Basic / Quick Business Card

Quick easy design project!

Need a one sided basic business card that matches font & style of brand and bottle label for our gourmet condiment, Velvet Corwin Sauce. Velvet Corwin Sauce is sold in specialty retail, gourmet groceries and appears on chef-driven restaurant menus, so the target market is a high end, gourmet, artisan-made food-loving customer.

Files Included:
Sauce Bottle Label
Velvet Corwin Sauce Round Logos

**About the logos - the logo may be used in a circle or alone vertically as on side of the bottle label**

Layout of Card:
May be vertical or horizontal based on designer ideas.

Logo usage (in circle vs. stand alone vertical logo) is up to designers descretion as well.

Reverse side of business card will be various high end / professional product photos / food shots using us.zelk.com system. **Designer on this project will NOT design a reserve for the card.**

Paper that will be used for printing:
Zelk Classic - it's a WHITE paper, but we use a cream background on Velvet Corwin Sauce branding, so please take this into account on design to stay brand consistent.

Elements & Copy for Card:
1. Logo in either script horizontal or vertical version
2. Copy: "Artisan Made - Small Batch"
3. Name - Rory Whitlock
4. Title - Creator
5. Phone - xxx.xxx.xxxx
6. xxxx@velvetcorwin.com
7. URL: velvetcorwinsauce.com
8. Social Media: @getvelvetcorwin on Twitter / Facebook / Instagram

Please provide final files in Illustrator or InDesign format.

```html
<!DOCTYPE html>
<html lang="en">
<head>
<meta charset="utf-8">
<title>Velvet Corwin Sauce – Business Card</title>
<link href="https://fonts.googleapis.com/css2?family=Open+Sans:wght@400;600;700&display=swap" rel="stylesheet">
<style>
  :root {
    --brand-yellow: #f2b21b;
    --brand-dark: #231f20;
    --card-white: #ffffff;
    --page-bg: #e6e4e0;
    --text-dark: #231f20;
  }
  html, body {
    margin: 0;
    padding: 0;
    width: 1200px;
    height: 804px;
    overflow: hidden;
    background: var(--page-bg);
    font-family: "Open Sans", Arial, sans-serif;
  }
  .business-card {
    position: absolute;
    left: 75px;
    top: 102px;
    width: 1050px;
    height: 600px;
    background: var(--card-white);
    box-shadow: 0 6px 24px rgba(0,0,0,0.18);
    overflow: hidden;
  }
  .card-shapes {
    position: absolute;
    inset: 0;
    width: 1050px;
    height: 600px;
  }
  .brand-mark {
    position: absolute;
    left: 70px;
    top: 100px;
    width: 280px;
    height: 280px;
    display: flex;
    flex-direction: column;
    align-items: center;
    justify-content: center;
    color: var(--brand-yellow);
    font-weight: 600;
    font-size: 42px;
    line-height: 1.1;
    text-align: center;
  }
  .tagline {
    position: absolute;
    left: 72px;
    top: 497px;
    font-size: 23px;
    color: var(--text-dark);
  }
  .contact-block {
    position: absolute;
    left: 582px;
    top: 165px;
    color: var(--text-dark);
  }
  .contact-name {
    margin: 0;
    font-size: 34px;
    font-weight: 700;
    line-height: 1.2;
  }
  .contact-title {
    margin: 2px 0 28px;
    font-size: 23px;
  }
  .contact-list {
    list-style: none;
    margin: 0;
    padding: 0;
  }
  .contact-list li {
    display: flex;
    align-items: center;
    gap: 8px;
    font-size: 21px;
    line-height: 36px;
  }
  .contact-icon {
    width: 18px;
    height: 18px;
    flex: none;
  }
  .follow-row {
    position: absolute;
    left: 622px;
    top: 490px;
    display: flex;
    align-items: center;
    gap: 12px;
    color: var(--card-white);
    font-size: 26px;
  }
  .social-dot {
    width: 30px;
    height: 30px;
    border-radius: 50%;
    background: var(--card-white);
  }
</style>
</head>
<body>
  <div class="business-card">
    <svg class="card-shapes" viewBox="0 0 1050 600" aria-hidden="true">
      <circle cx="210" cy="240" r="140" fill="var(--brand-dark)"/>
      <polyline points="550,470 550,160 650,62 1000,152 1000,460" fill="none" stroke="var(--brand-yellow)" stroke-width="10" stroke-linejoin="miter"/>
      <polygon points="300,528 580,528 566,542 290,542" fill="var(--brand-yellow)"/>
      <polygon points="0,552 575,552 552,578 0,578" fill="var(--brand-yellow)"/>
      <polygon points="605,455 1050,455 1050,590 510,590" fill="var(--brand-dark)"/>
    </svg>

    <div class="brand-mark">
      <span>Velvet</span>
      <span>Corwin</span>
      <span>Sauce</span>
    </div>

    <div class="tagline">Artisan Made - Small Batch</div>

    <div class="contact-block">
      <h1 class="contact-name">Rory Whitlock</h1>
      <p class="contact-title">Creator</p>
      <ul class="contact-list">
        <li>
          <svg class="contact-icon" viewBox="0 0 20 20" aria-hidden="true"><circle cx="10" cy="10" r="9" fill="none" stroke="var(--text-dark)" stroke-width="1.6"/><path d="M7 5 L9 7 L8 9 Q9 11.5 11 12 L13 11 L15 13 L13 15 Q7 14.5 5.5 7 Z" fill="var(--text-dark)"/></svg>
          123-456-7890
        </li>
        <li>
          <svg class="contact-icon" viewBox="0 0 20 20" aria-hidden="true"><rect x="2" y="5" width="16" height="11" fill="var(--text-dark)"/><polyline points="2,5 10,11 18,5" fill="none" stroke="#fff" stroke-width="1.5"/></svg>
          rwhitlock@velvetcorwin.com
        </li>
        <li>
          <svg class="contact-icon" viewBox="0 0 20 20" aria-hidden="true"><circle cx="10" cy="10" r="8" fill="none" stroke="var(--text-dark)" stroke-width="1.6"/><ellipse cx="10" cy="10" rx="3.5" ry="8" fill="none" stroke="var(--text-dark)" stroke-width="1.4"/><line x1="2" y1="10" x2="18" y2="10" stroke="var(--text-dark)" stroke-width="1.4"/></svg>
          www.velvetcorwinsauce.com
        </li>
      </ul>
    </div>

    <div class="follow-row">
      <span>Follow Us On</span>
      <span class="social-dot" aria-hidden="true"></span>
      <span class="social-dot" aria-hidden="true"></span>
      <span class="social-dot" aria-hidden="true"></span>
    </div>
  </div>
</body>
</html>
```